We are full service plumbing contractors that are capable of performing all of your plumbing need...

A clean, crisp website that conveys we can handle any plumbing from drain cleaning, repairs, to new construction. But emphasis on Leak detection, under-slab and underground water service leaks, repairs, and reroutes. Leak detection by acoustical, Thermal, or tracer gas , methods.Also emphasize advanced drain cleaning technologies and equipment. Don't just poke ahole in the drain blockage, Clean the pipe, with our High pressure hydrojetters, or Chain knocker drain cables that expand to the width of the pipe being cleaned.

Number of Pages Required

5+ page

Font styles to use
Sans Serif

Requirements
Should not have
• Canned photos

```html
<!DOCTYPE html>
<html lang="en">
<head>
<meta charset="utf-8">
<title>Pipe Otters – Plumbing Service</title>
<link href="https://fonts.googleapis.com/css2?family=Michroma&family=Lato:wght@400;700;900&display=swap" rel="stylesheet">
<style>
:root{
  --blue:#0f4fa6;
  --blue-light:#2a7ee0;
  --blue-dark:#0a2f6b;
  --ink:#111318;
  --text:#333;
  --muted:#666;
  --grey:#f1f1f2;
  --white:#fff;
  --footer:#0b0e1a;
}
*{box-sizing:border-box;margin:0;padding:0}
html,body{width:1200px;height:5202px;overflow:hidden}
body{font-family:'Lato',sans-serif;color:var(--text);background:var(--white);position:relative}
.display{font-family:'Michroma',sans-serif;letter-spacing:2px;text-transform:uppercase;color:var(--ink)}
.btn{display:inline-block;height:40px;line-height:40px;padding:0 34px;border-radius:20px;background:linear-gradient(180deg,var(--blue-light),var(--blue));color:var(--white);font-size:13px;font-weight:700;text-transform:uppercase;letter-spacing:.5px}
.btn-dark{background:#161616}
.section-title{text-align:center;font-size:30px;position:absolute;left:0;width:1200px}

/* top bar */
.topbar{position:absolute;top:0;left:0;width:1200px;height:34px;background:var(--ink);color:#ddd;font-size:13px}
.topbar .contact{position:absolute;left:360px;top:9px;display:flex;gap:40px}
.topbar .contact span::before{content:"";display:inline-block;width:8px;height:8px;border-radius:50%;background:var(--blue-light);margin-right:8px}
.topbar .social{position:absolute;right:90px;top:11px;display:flex;gap:22px}
.dot{width:12px;height:12px;border-radius:50%;background:#cfd6e2;display:block}

/* nav */
.nav{position:absolute;top:34px;left:0;width:1200px;height:94px;background:var(--white)}
.brand{position:absolute;left:60px;top:22px;display:flex;align-items:center;gap:10px;font-family:'Lato',sans-serif;font-weight:900;font-size:30px;color:var(--blue-dark)}
.brand i{width:18px;height:18px;border-radius:50%;background:var(--blue)}
.menu{position:absolute;left:595px;top:36px;display:flex;gap:40px;font-size:14px;color:#444}
.menu .active{color:var(--blue);border-bottom:2px solid var(--blue);padding-bottom:6px}
.search{position:absolute;right:130px;top:36px}

/* hero */
.hero{position:absolute;top:128px;left:0;width:1200px;height:640px;background:linear-gradient(180deg,#bfc2c4 0%,#9ea3a7 55%,#7f868c 100%)}
.hero h1{position:absolute;top:205px;width:1200px;text-align:center;color:var(--white);font-size:66px;letter-spacing:6px}
.hero h2{position:absolute;top:290px;width:1200px;text-align:center;color:var(--white);font-size:22px;letter-spacing:3px}
.hero .actions{position:absolute;top:355px;width:1200px;display:flex;justify-content:center;gap:22px}
.hero .scroll{position:absolute;left:590px;top:560px;width:20px;height:32px;border:2px solid #fff;border-radius:10px}
.hero .wave{position:absolute;left:0;top:565px}

/* features */
.features{position:absolute;top:850px;left:0;width:1200px;display:flex;justify-content:center;gap:58px}
.feature{width:200px;text-align:center}
.icon-circle{width:104px;height:104px;border-radius:50%;background:radial-gradient(circle at 40% 35%,var(--blue-light),var(--blue-dark));margin:0 auto 22px;display:flex;align-items:center;justify-content:center;box-shadow:0 4px 10px rgba(0,0,0,.2)}
.feature h3{font-size:18px;color:var(--ink);font-weight:900;margin-bottom:14px}
.feature p{font-size:13px;color:var(--muted);line-height:1.45}

/* services */
.services{position:absolute;top:1172px;left:0;width:1200px;height:590px;background:var(--grey)}
.services .section-title{top:50px}
.service{position:absolute;width:330px;display:flex;align-items:center;gap:18px}
.service .ic{flex:none;width:66px;height:66px;border-radius:50%;background:radial-gradient(circle at 40% 35%,var(--blue-light),var(--blue-dark));display:flex;align-items:center;justify-content:center}
.service h4{font-size:18px;color:var(--ink);font-weight:900;margin-bottom:8px}
.service p{font-size:13px;color:var(--muted);line-height:1.45}
.service.left{left:120px;text-align:right}
.service.right{left:760px}
.plumber{position:absolute;left:500px;top:92px;width:250px;height:498px;background:linear-gradient(180deg,#4f6e8c 0%,#2f4f6f 60%,#1d2f45 100%);border-radius:120px 120px 0 0}

/* projects */
.projects{position:absolute;top:1762px;left:0;width:1200px;height:860px;background:var(--ink)}
.projects .section-title{top:50px;color:var(--white)}
.grid{position:absolute;top:140px;left:0;width:1200px;display:grid;grid-template-columns:repeat(3,400px);grid-template-rows:repeat(2,295px)}
.grid div:nth-child(1){background:linear-gradient(135deg,#5a3b2a,#a27b55)}
.grid div:nth-child(2){background:linear-gradient(135deg,#4a4e3a,#8a8f74)}
.grid div:nth-child(3){background:linear-gradient(135deg,#9a9a98,#555a5f)}
.grid div:nth-child(4){background:linear-gradient(135deg,#3a2e22,#6d5a42)}
.grid div:nth-child(5){background:linear-gradient(135deg,#6e6050,#c4b8a8)}
.grid div:nth-child(6){background:linear-gradient(135deg,#8a8a86,#4f4f4c)}
.projects .btn{position:absolute;top:785px;left:508px}

/* about */
.about{position:absolute;top:2662px;left:0;width:1200px;height:376px;background:var(--white)}
.about h2{position:absolute;left:120px;top:82px;font-size:24px}
.about p{position:absolute;left:120px;top:142px;width:440px;font-size:13px;line-height:1.5;color:var(--muted)}
.about .btn{position:absolute;left:120px;top:250px}
.video{position:absolute;left:597px;top:0;width:603px;height:376px;background:linear-gradient(135deg,#d8d6d2,#8e8a84)}
.video .play{position:absolute;left:266px;top:153px;width:70px;height:70px;border-radius:50%;background:rgba(255,255,255,.85)}
.video .play::after{content:"";position:absolute;left:27px;top:21px;border-left:22px solid var(--ink);border-top:14px solid transparent;border-bottom:14px solid transparent}

/* blog */
.blog{position:absolute;top:3038px;left:0;width:1200px;height:766px}
.blog .section-title{top:78px}
.cards{position:absolute;top:152px;left:120px;display:flex;gap:14px}
.card{width:310px;background:var(--grey)}
.card .thumb{height:195px}
.card:nth-child(1) .thumb{background:linear-gradient(135deg,#5b4733,#8e7a5c)}
.card:nth-child(2) .thumb{background:linear-gradient(135deg,#3a2a6d,#c04a8a)}
.card:nth-child(3) .thumb{background:linear-gradient(135deg,#a7a7a5,#595c60)}
.card .body{padding:22px 26px 24px}
.card h5{font-family:'Michroma',sans-serif;font-size:13px;color:var(--ink);margin-bottom:6px}
.card .meta{font-size:11px;color:var(--muted);display:flex;gap:40px;margin-bottom:14px}
.card p{font-size:13px;line-height:1.45;color:var(--muted);margin-bottom:16px}
.blog .btn{position:absolute;top:652px;left:518px}

/* testimonials */
.clients{position:absolute;top:3804px;left:0;width:1200px;height:462px;background:linear-gradient(180deg,#2c2c2c,#161616 50%,#2a2a2a)}
.clients .section-title{top:90px;color:var(--white)}
.quote{position:absolute;top:152px;left:270px;width:660px;text-align:center;color:#ddd;font-size:14px;line-height:1.5}
.qmark{position:absolute;font-family:Georgia,serif;font-size:64px;color:#fff;top:130px}
.clients h6{position:absolute;top:212px;width:1200px;text-align:center;color:#fff;font-family:'Michroma',sans-serif;font-size:14px}
.stars{position:absolute;top:236px;width:1200px;text-align:center;color:#f3b51c;font-size:13px;letter-spacing:2px}
.pager{position:absolute;top:274px;width:1200px;display:flex;justify-content:center;gap:14px}
.pager i{width:7px;height:7px;border-radius:50%;background:#777}
.pager i.on{background:#fff}
.clients .btn{position:absolute;top:356px;left:520px}

/* form */
.request{position:absolute;top:4266px;left:0;width:1200px;height:520px}
.request .section-title{top:84px}
.field{position:absolute;height:40px;border:1px solid #cfd3da;border-radius:20px;padding-left:18px;line-height:38px;font-size:12px;color:#999;width:250px}
.field.msg{height:98px;border-radius:14px;width:513px;line-height:30px}
.request .submit{position:absolute;left:347px;top:466px;width:513px;text-align:center}

/* footer */
.footer{position:absolute;top:4786px;left:0;width:1200px;height:416px;background:var(--footer);color:#bbb}
.footer .wave{position:absolute;top:-20px;left:0}
.footer .brand{top:60px;left:120px;color:#fff;font-size:26px}
.footer .about-text{position:absolute;left:120px;top:112px;width:200px;font-size:13px;line-height:1.45}
.footer .soc{position:absolute;left:120px;top:180px;display:flex;gap:16px}
.footer h4{position:absolute;top:110px;font-family:'Michroma',sans-serif;font-size:16px;color:#fff;letter-spacing:2px}
.links{position:absolute;top:150px;list-style:none;font-size:13px;line-height:22px}
.links li::before{content:"›";margin-right:10px;color:var(--blue-light)}
.contact-list{position:absolute;left:607px;top:150px;list-style:none;font-size:13px;line-height:22px}
.contact-list li::before{content:"";display:inline-block;width:7px;height:7px;border-radius:50%;background:var(--blue-light);margin-right:10px}
.newsletter input{position:absolute;left:832px;top:152px;width:250px;height:40px;border-radius:20px;border:none;padding-left:18px;font-family:'Lato',sans-serif;font-size:12px}
.newsletter .btn{position:absolute;left:832px;top:202px;width:250px;text-align:center}
.footer .bar{position:absolute;top:330px;left:120px;width:960px;border-top:1px solid #2b3045}
.footer .copy{position:absolute;top:358px;left:120px;font-size:13px}
.footer .legal{position:absolute;top:358px;right:120px;font-size:13px}
</style>
</head>
<body>

<header class="topbar">
  <div class="contact"><span>(555) 014 2270</span><span>info@pipeotters.com</span></div>
  <div class="social"><i class="dot"></i><i class="dot"></i><i class="dot"></i><i class="dot"></i></div>
</header>

<nav class="nav">
  <div class="brand"><i></i>Pipe Otters</div>
  <div class="menu"><span class="active">Home</span><span>About</span><span>Services</span><span>Projects</span><span>Blogs</span><span>Contact</span></div>
  <svg class="search" width="18" height="18" viewBox="0 0 18 18"><circle cx="7.5" cy="7.5" r="6" fill="none" stroke="#333" stroke-width="2"/><line x1="12" y1="12" x2="17" y2="17" stroke="#333" stroke-width="2"/></svg>
</nav>

<section class="hero" role="img" aria-label="Bright modern bathroom with bathtub and wall mounted fixtures">
  <h1 class="display">Plumbing</h1>
  <h2 class="display">Service for your need</h2>
  <div class="actions"><span class="btn">Read more</span><span class="btn btn-dark">Request an appoinment</span></div>
  <div class="scroll"></div>
  <svg class="wave" width="1200" height="80" viewBox="0 0 1200 80"><path d="M0 20 Q600 90 1200 10 L1200 80 L0 80Z" fill="#fff"/><path d="M0 20 Q600 90 1200 10 L1200 30 Q600 100 0 40Z" fill="#1a5fc2"/><path d="M0 40 Q600 100 1200 30 L1200 40 Q600 108 0 50Z" fill="#0a2f6b"/></svg>
</section>

<section class="features">
  <div class="feature">
    <div class="icon-circle"><svg width="40" height="40" viewBox="0 0 24 24"><path d="M6.6 10.8a15 15 0 0 0 6.6 6.6l2.2-2.2c.3-.3.7-.4 1-.2 1.1.4 2.3.6 3.6.6.6 0 1 .4 1 1V20c0 .6-.4 1-1 1A17 17 0 0 1 3 4c0-.6.4-1 1-1h3.5c.6 0 1 .4 1 1 0 1.3.2 2.5.6 3.6.1.3 0 .7-.2 1z" fill="#fff"/></svg></div>
    <h3>Emergency Service</h3><p>Lorem Ipsum is simply dummy text of the printing and typesetting industry.</p>
  </div>
  <div class="feature">
    <div class="icon-circle"><svg width="40" height="40" viewBox="0 0 24 24"><rect x="3" y="6" width="14" height="5" rx="1" fill="#fff"/><rect x="9" y="2" width="2" height="4" fill="#fff"/><rect x="13" y="9" width="5" height="5" fill="#fff"/><path d="M16 17c0 2 1 3 1.5 3s1.5-1 1.5-3l-1.5-2z" fill="#fff"/></svg></div>
    <h3>Quality Materials</h3><p>Lorem Ipsum is simply dummy text of the printing and typesetting industry.</p>
  </div>
  <div class="feature">
    <div class="icon-circle"><svg width="40" height="40" viewBox="0 0 24 24"><path d="M4 20 14 10M14 10a4 4 0 1 0 2-5l-2 2 1 2 2 1 2-2a4 4 0 0 1-5 2" stroke="#fff" stroke-width="2.4" fill="none" stroke-linecap="round"/><path d="M4 4l7 7" stroke="#fff" stroke-width="2.4" stroke-linecap="round"/></svg></div>
    <h3>Repair Service</h3><p>Lorem Ipsum is simply dummy text of the printing and typesetting industry.</p>
  </div>
  <div class="feature">
    <div class="icon-circle"><svg width="40" height="40" viewBox="0 0 24 24"><path d="M12 3l2.7 5.6 6.1.9-4.4 4.3 1 6.1L12 17l-5.4 2.9 1-6.1L3.2 9.5l6.1-.9z" fill="#fff"/></svg></div>
    <h3>Satisfaction Gurantee</h3><p>Lorem Ipsum is simply dummy text of the printing and typesetting industry.</p>
  </div>
</section>

<section class="services">
  <h2 class="section-title display">Our Services</h2>
  <div class="plumber" role="img" aria-label="Plumber in work shirt and hard hat holding a tool case"></div>
  <div class="service left" style="top:150px"><div><h4>Drain Cleaning</h4><p>Lorem Ipsum is simply dummy text of the printing and typesetting industry.</p></div><span class="ic"><svg width="30" height="30" viewBox="0 0 24 24"><circle cx="12" cy="12" r="8" fill="none" stroke="#fff" stroke-width="2"/><circle cx="12" cy="12" r="3" fill="#fff"/></svg></span></div>
  <div class="service left" style="top:298px"><div><h4>Repair Service</h4><p>Lorem Ipsum is simply dummy text of the printing and typesetting industry.</p></div><span class="ic"><svg width="30" height="30" viewBox="0 0 24 24"><path d="M5 19 15 9M15 9a3.5 3.5 0 1 0 2-4" stroke="#fff" stroke-width="2.4" fill="none" stroke-linecap="round"/></svg></span></div>
  <div class="service left" style="top:446px"><div><h4>Reroutes</h4><p>Lorem Ipsum is simply dummy text of the printing and typesetting industry.</p></div><span class="ic"><svg width="30" height="30" viewBox="0 0 24 24"><path d="M4 6h8v12h8" stroke="#fff" stroke-width="3" fill="none"/></svg></span></div>
  <div class="service right" style="top:150px"><span class="ic"><svg width="30" height="30" viewBox="0 0 24 24"><path d="M3 10h12v4H3z" fill="#fff"/><path d="M18 14c0 2 .8 3 1.5 3s1.5-1 1.5-3l-1.5-2z" fill="#fff"/></svg></span><div><h4>Leak detection</h4><p>Lorem Ipsum is simply dummy text of the printing and typesetting industry.</p></div></div>
  <div class="service right" style="top:298px"><span class="ic"><svg width="30" height="30" viewBox="0 0 24 24"><path d="M4 8h16M4 12h16M4 16h16" stroke="#fff" stroke-width="2"/><path d="M12 4v16" stroke="#fff" stroke-width="2"/></svg></span><div><h4>Under-slab</h4><p>Lorem Ipsum is simply dummy text of the printing and typesetting industry.</p></div></div>
  <div class="service right" style="top:446px"><span class="ic"><svg width="30" height="30" viewBox="0 0 24 24"><path d="M3 8h18" stroke="#fff" stroke-width="2"/><path d="M6 14h12v4H6z" fill="#fff"/></svg></span><div><h4>Underground water Leak</h4><p>Lorem Ipsum is simply dummy text of the printing and typesetting industry.</p></div></div>
</section>

<section class="projects">
  <h2 class="section-title display">Recently Projects</h2>
  <div class="grid">
    <div role="img" aria-label="Copper pipe repair in wall"></div>
    <div role="img" aria-label="Plumber working in crawl space"></div>
    <div role="img" aria-label="Water heater installation"></div>
    <div role="img" aria-label="Excavated underground pipe"></div>
    <div role="img" aria-label="Technician at outdoor pipe trench"></div>
    <div role="img" aria-label="New yellow gas line on floor"></div>
  </div>
  <span class="btn">View all projects</span>
</section>

<section class="about">
  <h2 class="display">About us</h2>
  <p>Lorem Ipsum is simply dummy text of the printing and typesetting industry. Lorem Ipsum has been the industry's standard dummy text ever since the 1500s, when an unknown printer took a galley of type and scrambled it to make a type specimen book.</p>
  <span class="btn">Read more</span>
  <div class="video" role="img" aria-label="Video of technician with drain cleaning machine"><span class="play"></span></div>
</section>

<section class="blog">
  <h2 class="section-title display">Blog Posts</h2>
  <div class="cards">
    <article class="card"><div class="thumb" role="img" aria-label="Pipe leak in soil"></div><div class="body"><h5>BLOG POSTS</h5><div class="meta"><span>4.02.2019</span><span>Comments ( 34 )</span></div><p>Lorem Ipsum is simply dummy text of the printing and typesetting industry. Lorem Ipsum has been the industry's standard dummy text ever since the 1500s.</p><svg width="26" height="10" viewBox="0 0 26 10"><path d="M0 5h24M19 1l5 4-5 4" stroke="#111" stroke-width="1.6" fill="none"/></svg></div></article>
    <article class="card"><div class="thumb" role="img" aria-label="Thermal image of hidden leak"></div><div class="body"><h5>BLOG POSTS</h5><div class="meta"><span>4.02.2019</span><span>Comments ( 34 )</span></div><p>Lorem Ipsum is simply dummy text of the printing and typesetting industry. Lorem Ipsum has been the industry's standard dummy text ever since the 1500s.</p><svg width="26" height="10" viewBox="0 0 26 10"><path d="M0 5h24M19 1l5 4-5 4" stroke="#111" stroke-width="1.6" fill="none"/></svg></div></article>
    <article class="card"><div class="thumb" role="img" aria-label="Drain cleaning equipment on site"></div><div class="body"><h5>BLOG POSTS</h5><div class="meta"><span>4.02.2019</span><span>Comments ( 34 )</span></div><p>Lorem Ipsum is simply dummy text of the printing and typesetting industry. Lorem Ipsum has been the industry's standard dummy text ever since the 1500s.</p><svg width="26" height="10" viewBox="0 0 26 10"><path d="M0 5h24M19 1l5 4-5 4" stroke="#111" stroke-width="1.6" fill="none"/></svg></div></article>
  </div>
  <span class="btn">View more</span>
</section>

<section class="clients" role="img" aria-label="Dark close-up of metal pipes in background">
  <h2 class="section-title display">Our Clients Say's</h2>
  <span class="qmark" style="left:236px">“</span>
  <p class="quote">Lorem Ipsum is simply dummy text of the printing and typesetting industry. Lorem Ipsum has been the industry's standard dummy text ever since the 1500s.</p>
  <span class="qmark" style="left:918px">”</span>
  <h6>Daniel Moore</h6>
  <div class="stars">★★★★★</div>
  <div class="pager"><i></i><i class="on"></i><i></i></div>
  <span class="btn">View more</span>
</section>

<section class="request">
  <h2 class="section-title display">Request an appoinment</h2>
  <div class="field" style="left:347px;top:178px">First Name</div>
  <div class="field" style="left:610px;top:178px">Last Name</div>
  <div class="field" style="left:347px;top:234px">Email Address</div>
  <div class="field" style="left:610px;top:234px">Phone#</div>
  <div class="field msg" style="left:347px;top:290px">Message</div>
  <span class="btn submit">Submit now</span>
</section>

<footer class="footer">
  <svg class="wave" width="1200" height="50" viewBox="0 0 1200 50"><path d="M0 0 Q600 60 1200 0 L1200 50 L0 50Z" fill="#0b0e1a"/><path d="M0 0 Q600 60 1200 0 L1200 14 Q600 74 0 14Z" fill="#1a5fc2"/></svg>
  <div class="brand"><i></i>Pipe Otters</div>
  <p class="about-text">Lorem Ipsum is simply dummy text of the printing and typesetting industry.</p>
  <div class="soc"><i class="dot"></i><i class="dot"></i><i class="dot"></i><i class="dot"></i><i class="dot"></i></div>
  <h4 style="left:381px">Quick Links</h4>
  <ul class="links" style="left:381px"><li>Home</li><li>About us</li><li>Services</li><li>Reviews</li><li>Blogs</li><li>Contact us</li></ul>
  <h4 style="left:607px">Quick Links</h4>
  <ul class="contact-list"><li>(555) 014 2270</li><li>(555) 014 2271</li><li>info@pipeotters.com</li><li>48 Harbor Ln,</li><li>Seabrook Point,</li><li>NJ 07000</li></ul>
  <h4 style="left:832px">Newsletter</h4>
  <div class="newsletter"><input type="text" placeholder="Email Address"><span class="btn">Subscribe</span></div>
  <div class="bar"></div>
  <p class="copy">Copyright © 2019 Pipe Otters . All rights reserved.</p>
  <p class="legal">Privacy Policy · Terms &amp; conditions</p>
</footer>

</body>
</html>
```